Family Ranch with a hobby vineyard needs 2 wine labels for our first harvest

Design 2 wine labels (front and back) with the Brindor Ranch logo.
Label 1:
Sauvignon Blanc
Alc. 12.5% by Vol.
Palos Verdes Peninsula - add as the region
Year 2022
Label 2:
Cabernet Sauvignon
Alc. 13.5% by Vol.
Year 2022
For the back label design:
GOVERNMENT WARNING: (1) According to the Surgeon General, women
should not drink alcoholic beverages during pregnancy because of the risk of
birth defects. (2) Consumption of alcoholic beverages impairs your ability to
drive a car or operate machinery, and may cause health problems.
Contains Sulfates.
750ML
I just received the bottles and have attached a picture.
Look and feel
Each slider illustrates characteristics of the customer's brand and the style your logo design should communicate.

```html
<!DOCTYPE html>
<html lang="en">
<head>
<meta charset="utf-8">
<title>Brindor Ranch – Back Label</title>
<link href="https://fonts.googleapis.com/css2?family=Roboto+Condensed:wght@400;700&display=swap" rel="stylesheet">
<style>
  :root {
    --wine: #3a0a10;
    --wine-deep: #2a070b;
    --ink: #111111;
    --brand-ink: #1c0a0c;
    --paper: #e6e6e6;
    --icon-ring: #8a8a8a;
    --horse-light: #6b3a3c;
  }
  * { margin: 0; padding: 0; box-sizing: border-box; }
  html, body { width: 1200px; height: 2696px; overflow: hidden; }
  body { font-family: "Roboto Condensed", "Arial Narrow", sans-serif; color: var(--ink); background: var(--paper); }
  .label { position: relative; width: 1200px; height: 2696px; }

  .label__band { position: absolute; left: 0; top: 0; width: 1200px; height: 1497px; background: var(--wine); }
  .label__horse {
    position: absolute; left: 0; top: 1055px; width: 432px; height: 442px;
    background: radial-gradient(ellipse at 55% 45%, var(--horse-light) 0%, var(--wine-deep) 55%, var(--wine) 80%);
    opacity: .85;
  }
  .brand {
    position: absolute; left: 486px; top: 1240px; width: 600px;
    text-align: center; color: var(--brand-ink);
    font-weight: 400; font-size: 84px; line-height: 1; letter-spacing: 2px;
  }

  .label__panel { position: absolute; left: 0; top: 1497px; width: 1200px; height: 1199px; background: var(--paper); }
  .warning { position: absolute; left: 122px; top: 1635px; width: 955px; }
  .warning__title { font-weight: 700; font-size: 44px; text-align: center; margin-bottom: 22px; }
  .warning__item { margin-bottom: 20px; }
  .warning__line { display: block; font-size: 41px; line-height: 63px; text-align: justify; text-align-last: justify; white-space: nowrap; }
  .warning__line--last { text-align-last: left; }

  .drinks { position: absolute; left: 110px; top: 2236px; }
  .specs { position: absolute; left: 370px; top: 2232px; font-size: 41px; line-height: 56px; }
  .specs__volume { font-size: 130px; line-height: 1; margin-top: 2px; letter-spacing: -1px; }
  .pregnancy-icon { position: absolute; left: 887px; top: 2376px; }
</style>
</head>
<body>
<main class="label">
  <section class="label__band">
    <div class="label__horse" role="img" aria-label="Engraved illustration of a horse head with bridle"></div>
    <div class="brand">BRINDOR RANCH</div>
  </section>

  <section class="label__panel"></section>

  <section class="warning">
    <h2 class="warning__title">GOVERNMENT WARNING:</h2>
    <p class="warning__item">
      <span class="warning__line">(1) ACCORDING TO THE SURGEON GENERAL, WOMEN</span>
      <span class="warning__line">SHOULD NOT DRINK ALCOHOLIC BEVERAGES DURING</span>
      <span class="warning__line">PREGNANCY BECAUSE OF THE RISK OF BIRTH DEFECTS.</span>
    </p>
    <p class="warning__item">
      <span class="warning__line">(2) CONSUMPTION OF ALCOHOLIC BEVERAGES</span>
      <span class="warning__line">IMPAIRS YOUR ABILITY TO DRIVE A CAR OR OPERATE</span>
      <span class="warning__line warning__line--last">MACHINERY, AND MAY CAUSE HEALTH PROBLEMS.</span>
    </p>
  </section>

  <svg class="drinks" width="200" height="300" viewBox="0 0 200 300" aria-label="8.3 standard drinks">
    <text transform="translate(40 290) rotate(-90)" font-family="Roboto Condensed, sans-serif" font-weight="700" font-size="40" fill="#111">Standard Drinks</text>
    <path d="M70 6 H190 V90 Q190 165 130 172 Q70 165 70 90 Z" fill="#111"/>
    <rect x="124" y="170" width="12" height="110" fill="#111"/>
    <rect x="72" y="274" width="116" height="12" fill="#111"/>
    <rect x="80" y="14" width="100" height="8" fill="#e6e6e6"/>
    <text x="130" y="100" text-anchor="middle" font-family="Roboto Condensed, sans-serif" font-weight="700" font-size="58" fill="#e6e6e6">8.3</text>
  </svg>

  <div class="specs">
    <p>CONTAINS SULFATES.</p>
    <p>12.5% ALC/VOL</p>
    <p>WINE OF USA</p>
    <p class="specs__volume">750ml</p>
  </div>

  <svg class="pregnancy-icon" width="164" height="164" viewBox="0 0 164 164" role="img" aria-label="No drinking during pregnancy symbol">
    <circle cx="82" cy="82" r="76" fill="#111" stroke="#8a8a8a" stroke-width="10"/>
    <line x1="40" y1="22" x2="124" y2="142" stroke="#8a8a8a" stroke-width="10"/>
  </svg>
</main>
</body>
</html>
```